Zielgruppe
Ich bin eine junge Fotografin und tätig in folgenden Bereichen:
- Hochzeits-Fotografie
- Outdoor-Fotografie
- Studio-Fotografie
Aufgabenstellung
Die Seite soll freundlich, professionell und übersichtlich sein.
Die Seite soll von den Bildern leben. Emotionen vermitteln.
Responsive Design ist mir wichtig, im nachhinein möchte ich die Seite Programmieren lassen damit ich mit Wordpress arbeiten kann und die Seite soll gut Suchmaschinenoptimiert werden.

```html
<!DOCTYPE html>
<html lang="de">
<head>
<meta charset="utf-8">
<title>Angebote – Velvet Lantern</title>
<link href="https://fonts.googleapis.com/css2?family=Open+Sans:wght@400;600;700&family=Roboto:wght@400&display=swap" rel="stylesheet">
<style>
:root{
  --red:#d60000;
  --text:#555;
  --light-bg:#f1f1f1;
  --row-bg:#f7f8f7;
  --line:#e4e4e4;
  --footer:#5a5a5a;
  --white:#fff;
}
*{box-sizing:border-box;margin:0;padding:0}
html,body{width:1200px;height:974px;overflow:hidden}
body{position:relative;background:var(--white);font-family:"Open Sans",Arial,sans-serif;color:var(--text)}
.site-header{position:absolute;left:0;top:0;width:1200px;height:60px;background:var(--white);border-top:2px solid var(--red);box-shadow:0 1px 3px rgba(0,0,0,.08);z-index:2}
.brand{position:absolute;left:200px;top:16px;font-family:"Open Sans",Arial,sans-serif;font-size:20px;font-weight:400;color:var(--text);letter-spacing:.5px;display:flex;align-items:center;gap:8px}
.brand-dot{width:14px;height:14px;border-radius:50%;background:var(--red)}
.main-nav{position:absolute;top:21px;left:0;width:1200px;font-family:Roboto,Arial,sans-serif;font-size:8.5px}
.main-nav a{position:absolute;color:#333;text-decoration:none;line-height:20px}
.main-nav a.active{background:var(--red);color:var(--white);padding:0 7px;border-radius:1px}
.offers{position:absolute;left:0;top:60px;width:1200px;height:689px;background:var(--light-bg);border-bottom:1px solid #dcdcdc}
.offers-title{position:absolute;top:31px;width:100%;text-align:center;font-size:15px;font-weight:400;color:var(--text)}
.title-rule{position:absolute;left:584px;top:63px;width:32px;height:2px;background:var(--red)}
.paper{position:absolute;top:120px;width:234px;height:526px;filter:drop-shadow(0 1px 3px rgba(0,0,0,.12))}
.paper-sheet{position:absolute;inset:0;background:var(--white);clip-path:polygon(0 0,194px 0,234px 60px,234px 526px,42px 526px,0 470px)}
.offer-table{position:absolute;left:16px;top:40px;width:202px;border:1px solid var(--line);border-top:none}
.offer-head{height:54px;background:var(--red);color:var(--white);font-weight:700;font-size:15px;text-align:center;line-height:54px}
.offer-desc{height:58px;background:var(--row-bg);border-bottom:1px solid var(--line);display:flex;align-items:center;justify-content:center;text-align:center;font-size:10px;line-height:17.5px;padding:0 6px}
.offer-price{height:39px;background:var(--white);border-bottom:1px solid var(--line);display:flex;align-items:center;justify-content:center;gap:5px;font-size:10px;font-weight:700;color:#444}
.offer-price:last-child{border-bottom:none}
.offer-price svg{width:18px;height:11px}
.section-notch{position:absolute;left:560px;top:726px;width:80px;height:25px;z-index:1}
.cta{position:absolute;left:535px;top:776px;width:130px;height:26px;background:var(--red);color:var(--white);font-size:8px;font-weight:700;text-align:center;line-height:26px;border-radius:1px}
.site-footer{position:absolute;left:0;top:824px;width:1200px;height:150px;background:var(--footer);color:var(--white);text-align:center;font-size:10px;line-height:17.2px;padding-top:16px}
.site-footer a{color:var(--white)}
.site-footer strong{font-weight:700}
.social-box{display:inline-block;width:18px;height:18px;background:#111;vertical-align:middle;margin-left:2px}
</style>
</head>
<body>
<header class="site-header">
  <div class="brand"><span>Velvet Lantern</span></div>
  <nav class="main-nav">
    <a style="left:708px">Willkommen</a>
    <a style="left:774px">Hinter der Linse</a>
    <a style="left:856px">Portfolio</a>
    <a class="active" style="left:899px">Angebote</a>
    <a style="left:963px">Kontakt</a>
  </nav>
</header>

<section class="offers">
  <h1 class="offers-title">Angebote</h1>
  <div class="title-rule"></div>

  <div class="paper" style="left:210px">
    <div class="paper-sheet"></div>
    <div class="offer-table">
      <div class="offer-head">Hochzeit</div>
      <div class="offer-desc">Angebotsbeschreibung Lorem ipsum sit amet</div>
      <div class="offer-price"><svg viewBox="0 0 18 11"><path d="M1 1v7h15M13 5l3 3-3 3" fill="none" stroke="#d60000" stroke-width="1.4"/></svg>xx,xx- €</div>
      <div class="offer-desc">Angebotsbeschreibung Lorem ipsum sit amet</div>
      <div class="offer-price"><svg viewBox="0 0 18 11"><path d="M1 1v7h15M13 5l3 3-3 3" fill="none" stroke="#d60000" stroke-width="1.4"/></svg>xx,xx- €</div>
      <div class="offer-desc">Angebotsbeschreibung Lorem ipsum sit amet</div>
      <div class="offer-price"><svg viewBox="0 0 18 11"><path d="M1 1v7h15M13 5l3 3-3 3" fill="none" stroke="#d60000" stroke-width="1.4"/></svg>xx,xx- €</div>
      <div class="offer-desc">Angebotsbeschreibung Lorem ipsum sit amet</div>
      <div class="offer-price"><svg viewBox="0 0 18 11"><path d="M1 1v7h15M13 5l3 3-3 3" fill="none" stroke="#d60000" stroke-width="1.4"/></svg>xx,xx- €</div>
    </div>
  </div>

  <div class="paper" style="left:483px">
    <div class="paper-sheet"></div>
    <div class="offer-table">
      <div class="offer-head">Outdoor</div>
      <div class="offer-desc">Angebotsbeschreibung Lorem ipsum sit amet</div>
      <div class="offer-price"><svg viewBox="0 0 18 11"><path d="M1 1v7h15M13 5l3 3-3 3" fill="none" stroke="#d60000" stroke-width="1.4"/></svg>xx,xx- €</div>
      <div class="offer-desc">Angebotsbeschreibung Lorem ipsum sit amet</div>
      <div class="offer-price"><svg viewBox="0 0 18 11"><path d="M1 1v7h15M13 5l3 3-3 3" fill="none" stroke="#d60000" stroke-width="1.4"/></svg>xx,xx- €</div>
      <div class="offer-desc">Angebotsbeschreibung Lorem ipsum sit amet</div>
      <div class="offer-price"><svg viewBox="0 0 18 11"><path d="M1 1v7h15M13 5l3 3-3 3" fill="none" stroke="#d60000" stroke-width="1.4"/></svg>xx,xx- €</div>
      <div class="offer-desc">Angebotsbeschreibung Lorem ipsum sit amet</div>
      <div class="offer-price"><svg viewBox="0 0 18 11"><path d="M1 1v7h15M13 5l3 3-3 3" fill="none" stroke="#d60000" stroke-width="1.4"/></svg>xx,xx- €</div>
    </div>
  </div>

  <div class="paper" style="left:756px">
    <div class="paper-sheet"></div>
    <div class="offer-table">
      <div class="offer-head">Studio</div>
      <div class="offer-desc">Angebotsbeschreibung Lorem ipsum sit amet</div>
      <div class="offer-price"><svg viewBox="0 0 18 11"><path d="M1 1v7h15M13 5l3 3-3 3" fill="none" stroke="#d60000" stroke-width="1.4"/></svg>xx,xx- €</div>
      <div class="offer-desc">Angebotsbeschreibung Lorem ipsum sit amet</div>
      <div class="offer-price"><svg viewBox="0 0 18 11"><path d="M1 1v7h15M13 5l3 3-3 3" fill="none" stroke="#d60000" stroke-width="1.4"/></svg>xx,xx- €</div>
      <div class="offer-desc">Angebotsbeschreibung Lorem ipsum sit amet</div>
      <div class="offer-price"><svg viewBox="0 0 18 11"><path d="M1 1v7h15M13 5l3 3-3 3" fill="none" stroke="#d60000" stroke-width="1.4"/></svg>xx,xx- €</div>
      <div class="offer-desc">Angebotsbeschreibung Lorem ipsum sit amet</div>
      <div class="offer-price"><svg viewBox="0 0 18 11"><path d="M1 1v7h15M13 5l3 3-3 3" fill="none" stroke="#d60000" stroke-width="1.4"/></svg>xx,xx- €</div>
    </div>
  </div>
</section>

<svg class="section-notch" viewBox="0 0 80 25" aria-hidden="true">
  <path d="M0 24 C18 24 28 18 34 4 Q40 -1 46 4 C52 18 62 24 80 24 L80 25 L0 25Z" fill="#fff" stroke="#dcdcdc" stroke-width="1"/>
  <path d="M35 12 l5 5 5-5" fill="none" stroke="#c8c8c8" stroke-width="2.2"/>
</svg>

<a class="cta">Jetzt Kontakt aufnehmen</a>

<footer class="site-footer">
  <p>© www.velvet-lantern.ch. Alle Rechte vorbehalten. <a>AGB</a> I <a>Links</a></p>
  <p><strong>Velvet Lantern | Fotografie</strong></p>
  <p><strong>Lena Marbach</strong></p>
  <p>Lindenweg 14</p>
  <p>6300 Musterdorf</p>
  <p>Mobile: 079 555 01 23</p>
  <p>Netzwerk:<span class="social-box"></span></p>
</footer>
</body>
</html>
```